Technology Project Portal - Project Listing portal

We require a logo & website designed for our new project.

Project Name: lumafold
Description:
We have a webapp where clients and service providers can come, signup and register development projects. Service providers can the browse projects and contact clients via the portal

Design brief:
Clean & Modern - See Attached color palet & style references. (Feel free to try alternative color palets)

See Project Proposal for site requirements.
UX flow section details pages requires

Examples of all standard UI Components required e.g.
text box / field
Drop down
date picker
etc..

Target Market(s)

Business / Technology providers

Logo Text

LumaFold

Coding

Coded - Design and coding required

Number of Pages Required

5+ page

Requirements
Must have
• Clean Modern Design
Examples for all common UI elements
Templates for common Web App Dialogs e.g. Confirm Delete/Logout etc

```html
<!DOCTYPE html>
<html lang="en">
<head>
<meta charset="utf-8">
<title>lumafold – Sign In</title>
<link rel="stylesheet" href="https://fonts.googleapis.com/css2?family=Poppins:wght@300;400;500&display=swap">
<style>
  :root {
    --brand: #ff3d00;
    --brand-deep: #d9431e;
    --brand-soft: #f7693a;
    --ink: #6f6f73;
    --muted: #a9a9ad;
    --rule: #c9c9cc;
    --button-grey: #85858a;
    --paper: #ffffff;
    --photo-top: #c9c4bd;
    --photo-mid: #6d6a66;
    --photo-low: #e9e7e4;
  }
  * { box-sizing: border-box; margin: 0; padding: 0; }
  html, body { width: 1200px; height: 702px; overflow: hidden; background: var(--paper); }
  body { position: relative; font-family: "Poppins", sans-serif; }

  .corner { position: absolute; }
  .corner--top { left: 0; top: 0; }
  .corner--bottom { left: 655px; top: 614px; }

  .login-card {
    position: absolute; left: 63px; top: 177px; width: 581px; height: 347px;
    display: flex; background: var(--paper);
    box-shadow: 0 2px 8px rgba(0,0,0,0.12);
    border: 1px solid #ececec;
  }
  .login-form { position: relative; width: 291px; height: 100%; }

  .welcome {
    position: absolute; left: 57px; top: 83px;
    font-size: 13.5px; font-weight: 400; color: var(--ink); letter-spacing: 0.1px;
  }
  .welcome .brand { color: var(--brand); }
  .tagline {
    position: absolute; left: 57px; top: 110px; width: 140px;
    font-size: 6.6px; font-weight: 300; line-height: 8px; color: var(--muted);
  }
  .steps { position: absolute; left: 57px; top: 135px; display: flex; gap: 2px; }
  .steps span { width: 24px; height: 1.4px; background: var(--button-grey); }
  .steps span:first-child { background: var(--brand); }

  .field {
    position: absolute; left: 57px; width: 176px; height: 18px;
    border-bottom: 1px solid var(--rule);
    display: flex; align-items: center; gap: 7px;
  }
  .field--user { top: 160px; }
  .field--pass { top: 184px; }
  .field svg { margin-left: 3px; flex: none; }
  .field input {
    border: none; outline: none; background: transparent;
    font-family: "Poppins", sans-serif; font-size: 6.8px; font-weight: 300; color: var(--ink); width: 140px;
  }
  .field input::placeholder { color: var(--muted); }

  .forgot {
    position: absolute; left: 56px; top: 208px;
    font-size: 7px; color: var(--brand); text-decoration: none;
  }
  .actions { position: absolute; left: 57px; top: 236px; display: flex; gap: 6px; }
  .btn {
    width: 85px; height: 23px; border: none;
    font-family: "Poppins", sans-serif; font-size: 7.6px; font-weight: 500; color: #fff;
  }
  .btn--primary { background: var(--brand); }
  .btn--secondary { background: var(--button-grey); }

  .brand-panel {
    position: relative; width: 290px; height: 100%;
    background: linear-gradient(180deg, var(--brand-deep) 0%, #e0522a 55%, var(--brand-soft) 100%);
    display: flex; align-items: center; justify-content: center;
  }
  .brand-panel .wordmark {
    color: #fff; font-size: 23px; font-weight: 400; letter-spacing: 0.2px; margin-top: -6px;
  }

  .showcase-photo {
    position: absolute; left: 740px; top: 0; width: 460px; height: 702px;
    background: linear-gradient(160deg, var(--photo-top) 0%, var(--photo-mid) 35%, #b9a9a0 60%, var(--photo-low) 100%);
  }
</style>
</head>
<body>
  <svg class="corner corner--top" width="79" height="81" aria-hidden="true"><polygon points="0,0 79,0 0,81" fill="var(--brand)"/></svg>
  <svg class="corner corner--bottom" width="85" height="88" aria-hidden="true"><polygon points="85,0 85,88 0,88" fill="var(--brand)"/></svg>

  <main class="login-card">
    <section class="login-form">
      <h1 class="welcome">Welcome to <span class="brand">lumafold</span></h1>
      <p class="tagline">We make it easy for everyone to invest in our company.</p>
      <div class="steps"><span></span><span></span></div>

      <label class="field field--user">
        <svg width="7" height="8" viewBox="0 0 14 16" aria-hidden="true"><circle cx="7" cy="5" r="3.8" fill="none" stroke="var(--brand)" stroke-width="1.6"/><path d="M1 15.5c0-3.5 2.7-5.5 6-5.5s6 2 6 5.5" fill="none" stroke="var(--brand)" stroke-width="1.6"/></svg>
        <input type="text" placeholder="User name">
      </label>
      <label class="field field--pass">
        <svg width="6" height="8" viewBox="0 0 12 16" aria-hidden="true"><path d="M3 7V4.5a3 3 0 0 1 6 0V7" fill="none" stroke="var(--brand)" stroke-width="1.6"/><rect x="1" y="7" width="10" height="8" rx="1" fill="none" stroke="var(--brand)" stroke-width="1.6"/><rect x="5.3" y="9.5" width="1.4" height="3" fill="var(--brand)"/></svg>
        <input type="password" placeholder="Password">
      </label>

      <a class="forgot" href="#">Forgot your&nbsp; password</a>

      <div class="actions">
        <button class="btn btn--primary">Sign In</button>
        <button class="btn btn--secondary">Sign Up</button>
      </div>
    </section>

    <section class="brand-panel" role="img" aria-label="Orange-tinted photo of a person working on a laptop at a wooden table in a loft office">
      <span class="wordmark">lumafold</span>
    </section>
  </main>

  <div class="showcase-photo" role="img" aria-label="Photo of a person at a desk using a laptop that shows the lumafold sign-in screen"></div>
</body>
</html>
```